Emergency Management Consulting Needs a Website

Need to develop a website for an Emergency Management Consulting business. This website needs to be user friendly and resemble disaster preparedness, response, recovery, and mitigation. It must allow for me to make changes to it myself by adding pages, content and pictures. Looking for an advanced page to the website that allows monitoring of social media sites, hashtags, and keywords. Must have pictures of disasters on the site. Must try to integrate the logo colors, not excessive.

Reason: Did not receive anything sufficient to what I am looking for.

Industry/Entity Type

Government

Coding

Coded - Design and coding required

Number of Pages Required

5+ page

Requirements
Must have
• Logo, advanced social media monitoring page, allow for edits myself (content, pages, graphics) this must be a CMS of some sort, use logo color scheme (not excessively), must be professional looking, connect with Vexlo Domain, find a hosting site, SEO, no "long" designs, minimize "dead" space, no social media feeds, no newsletter stuff.
• Menu items: Home, About Us, Services, Situation Monitor, Work With Us, Contact Us (hopefully these could be editable if I need to later)
• When you make a submission, please send me a message on which CMS you are using. Thank you.
Nice to have
• Examples of websites:
• https://www.plorn.vic.gov.au/
• http://www.garvelmunds.com/
• http://www.tqplaxr.org/
• http://dumbrellconsulting.com/
• http://www.folvantix.com/services/emergency-management
• https://qzu.com/
• http://www.belmorvia.com/Responsibility/Sustainable-Development/HSE/Crisis-and-Emergency-Management/

```html
<!DOCTYPE html>
<html lang="en">
<head>
<meta charset="utf-8">
<title>Stonebridge Emergency Management</title>
<link href="https://fonts.googleapis.com/css2?family=Open+Sans:wght@400;600;700&family=Raleway:wght@600;700&display=swap" rel="stylesheet">
<style>
:root{
  --orange:#e8892b;
  --ink:#333a40;
  --muted:#7a7f84;
  --band:#ebebeb;
  --footer:#3a3d40;
  --footer-deep:#2c2e30;
  --white:#ffffff;
}
*{box-sizing:border-box;margin:0;padding:0}
html,body{width:771px;height:1200px;overflow:hidden;background:var(--white)}
body{font-family:"Open Sans",Arial,sans-serif;color:var(--ink)}
.page{position:relative;width:771px;height:1200px;overflow:hidden}
.btn{display:inline-block;background:var(--orange);color:var(--white);font-size:8px;font-weight:700;letter-spacing:.8px;padding:7px 16px;text-transform:uppercase;border-radius:2px}

/* header */
.site-header{height:32px;display:flex;align-items:center;justify-content:space-between;padding:0 88px 0 96px;background:var(--white)}
.brand{display:flex;align-items:center;gap:6px;font-family:"Raleway",sans-serif;font-weight:700;font-size:16px;color:var(--ink);letter-spacing:.5px}
.brand-dot{width:14px;height:14px;border-radius:50%;background:var(--orange)}
.main-nav{display:flex;gap:16px;font-size:7px;font-weight:700;letter-spacing:.5px;align-items:center}
.main-nav a{color:var(--ink);text-decoration:none}
.main-nav a.active{color:var(--orange)}

/* hero */
.hero{position:relative;height:282px;background:linear-gradient(180deg,#b6bcc0 0%,#8d8a84 45%,#5a524b 80%,#3f3933 100%)}
.hero-copy{position:absolute;left:96px;top:150px}
.hero-title{font-family:"Raleway",sans-serif;font-weight:700;color:var(--white);font-size:20px;line-height:1.15;margin-bottom:12px}

/* intro */
.intro{height:150px;text-align:center;padding-top:24px}
.section-title{font-family:"Raleway",sans-serif;font-weight:700;font-size:15px;color:var(--ink)}
.intro p{width:430px;margin:8px auto 14px;font-size:7.5px;line-height:1.55;color:var(--muted)}

/* testimonial */
.testimonial{height:200px;background:var(--band);text-align:center;padding-top:28px;position:relative}
.avatars{display:flex;justify-content:center;align-items:center;gap:22px}
.avatar{width:22px;height:22px;border-radius:50%;background:#b9b3ad}
.avatar.featured{width:32px;height:32px;background:#a0938a}
.testimonial blockquote{width:440px;margin:16px auto 10px;font-size:7.5px;line-height:1.55;color:var(--muted)}
.testimonial cite{display:block;font-style:normal;font-size:7px;font-weight:700;letter-spacing:.8px;margin-bottom:2px}
.testimonial .role{display:block;font-size:6.5px;color:var(--muted);margin-bottom:12px}
.slider-arrow{position:absolute;top:92px;width:10px;height:14px}
.slider-arrow.prev{left:80px}
.slider-arrow.next{right:80px}

/* cases */
.cases{height:288px;text-align:center;padding-top:26px}
.cases .lede{font-size:7px;color:var(--muted);margin-top:4px}
.case-grid{display:flex;justify-content:center;gap:8px;margin-top:18px}
.case-card{position:relative;width:186px;height:150px;text-align:left;overflow:hidden}
.case-card.highlight{background:var(--orange);color:var(--white);padding:16px 14px}
.case-card.highlight h3{font-size:11px;font-weight:700}
.case-card.highlight h4{font-size:7px;font-weight:600;margin:2px 0 10px;opacity:.9}
.case-card.highlight p{font-size:6.5px;line-height:1.55}
.case-card.highlight .more{position:absolute;left:14px;bottom:12px;font-size:6.5px;font-weight:700}
.case-photo{position:absolute;inset:0}
.case-photo.campus{background:linear-gradient(180deg,#9fc2e0 0%,#c9c4b6 55%,#6f7d5a 100%)}
.case-photo.quarter{background:linear-gradient(180deg,#a8c9e4 0%,#d9d3c4 50%,#5f6e4f 100%)}
.case-label{position:absolute;left:12px;bottom:12px;color:var(--white);font-size:10px;font-weight:700}
.cases .btn{margin-top:18px}

/* footer */
.site-footer{height:248px;background:var(--footer);color:#c9cbcd;position:relative}
.footer-cols{display:flex;padding:28px 0 0 96px;gap:0}
.footer-col h5{font-family:"Raleway",sans-serif;color:var(--white);font-size:10px;font-weight:700;margin-bottom:10px}
.footer-col.links{width:340px}
.quick-links{list-style:none;font-size:6.5px;line-height:1.7}
.quick-links li:first-child{color:var(--orange)}
.contact{font-size:6.5px;line-height:1.6}
.contact .phone{color:var(--white);font-size:10px;font-weight:600;margin:2px 0 8px}
.footer-bar{position:absolute;left:0;right:0;bottom:0;height:30px;background:var(--footer-deep);display:flex;align-items:center;justify-content:space-between;padding:0 88px 0 96px;font-size:6.5px}
.social{display:flex;gap:4px}
.social span{width:11px;height:11px;border-radius:50%;background:#5b7fb0}
.social span:nth-child(2){background:#4aa3d8}
.social span:nth-child(3){background:#c9463d}
.social span:nth-child(4){background:#3f77a8}
.social span:nth-child(5){background:var(--orange)}
</style>
</head>
<body>
<div class="page">

  <header class="site-header">
    <div class="brand"><span class="brand-dot"></span>STONEBRIDGE</div>
    <nav class="main-nav">
      <a class="active" href="#">HOME</a>
      <a href="#">ABOUT US</a>
      <a href="#">SERVICES</a>
      <a href="#">SITUATION MONITOR</a>
      <a href="#">WORK WITH US</a>
      <a href="#">CONTACT US</a>
      <svg width="8" height="8" viewBox="0 0 10 10" aria-label="Search"><circle cx="4" cy="4" r="3" fill="none" stroke="#333a40" stroke-width="1.5"/><line x1="6.3" y1="6.3" x2="9.3" y2="9.3" stroke="#333a40" stroke-width="1.5"/></svg>
    </nav>
  </header>

  <section class="hero" role="img" aria-label="Photograph of a neighbourhood destroyed by wildfire with burnt cars and rubble">
    <div class="hero-copy">
      <h1 class="hero-title">We Help Clients Prepare<br>for Disasters.</h1>
      <span class="btn">Learn More</span>
    </div>
  </section>

  <section class="intro">
    <h2 class="section-title">Stonebridge Emergency Management</h2>
    <p>Our team has been the trusted partner of public agencies and private firms for over two decades, helping them plan for crises, respond with speed and rebuild stronger communities once the danger has passed.</p>
    <span class="btn">About Us</span>
  </section>

  <section class="testimonial">
    <div class="avatars">
      <span class="avatar" role="img" aria-label="Client portrait"></span>
      <span class="avatar featured" role="img" aria-label="Portrait of featured client"></span>
      <span class="avatar" role="img" aria-label="Client portrait"></span>
    </div>
    <svg class="slider-arrow prev" viewBox="0 0 10 14" aria-label="Previous"><polyline points="8,1 2,7 8,13" fill="none" stroke="#9a9a9a" stroke-width="1.5"/></svg>
    <svg class="slider-arrow next" viewBox="0 0 10 14" aria-label="Next"><polyline points="2,1 8,7 2,13" fill="none" stroke="#9a9a9a" stroke-width="1.5"/></svg>
    <blockquote>Their team guided our county through two major floods with calm, clear planning and steady support. I would recommend them to any agency that needs a partner they can trust when it matters most.</blockquote>
    <cite>- DANA FORELL -</cite>
    <span class="role">Director</span>
    <span class="btn">Meet The Team</span>
  </section>

  <section class="cases">
    <h2 class="section-title">We’ve Helped Thousands Across The United States.</h2>
    <p class="lede">Here is a sample of our work across the country.</p>
    <div class="case-grid">
      <article class="case-card highlight">
        <h3>Wilmington, NC</h3>
        <h4>Debris Monitor Oversight</h4>
        <p>Our team led debris planning and shelter logistics for the city after a major hurricane, restoring key services and safe roads within a few short weeks.</p>
        <span class="more">+ Read More</span>
      </article>
      <article class="case-card">
        <div class="case-photo campus" role="img" aria-label="Photograph of a columned university building"></div>
        <span class="case-label">University Park, PA</span>
      </article>
      <article class="case-card">
        <div class="case-photo quarter" role="img" aria-label="Photograph of a historic building with iron balconies"></div>
        <span class="case-label">New Orleans, LA</span>
      </article>
    </div>
    <span class="btn">See More Case Studies</span>
  </section>

  <footer class="site-footer">
    <div class="footer-cols">
      <div class="footer-col links">
        <h5>Quick Link</h5>
        <ul class="quick-links">
          <li>Home</li><li>About Us</li><li>Services</li><li>Situation Monitor</li><li>Work With Us</li><li>Contact Us</li>
        </ul>
      </div>
      <div class="footer-col contact">
        <h5>Contact Us</h5>
        <p>Need Help?</p>
        <p class="phone">Call Us: (555) 014-2290</p>
        <p>info@stonebridgeem.com</p>
        <p>Stonebridge Emergency Management<br>4120 Harlow Ave, Suite 200<br>Lorenton, IL 60401</p>
      </div>
    </div>
    <div class="footer-bar">
      <span>© 2017 Stonebridge Emergency Management. All Rights Reserved.</span>
      <div class="social"><span></span><span></span><span></span><span></span><span></span></div>
    </div>
  </footer>

</div>
</body>
</html>
```